Business Card for Dental Office

I need a business card that reflects a modern day dental office, called Heron Creek Dental. We specialize in general and Cosmetic Dentistry. On the front it must have the business information and the logo and the back side QR code and a place to note the appointment. I have attached the logo and a current business card for the information

Target Market(s)

Patients with Dental care need

Industry/Entity Type

Health Care

Contact Information for Business Card

Regular size business card with round corners

Font styles to use
Other font styles liked:
• lato light font

Colors
34a7d8
0255a3
ffffff
000000
85cae6
85acd3

Requirements
Must have
• The logo, business information, website and in the a place to write down the appointment
Nice to have
• QR Code in the back

```html
<!DOCTYPE html>
<html lang="en">
<head>
<meta charset="utf-8">
<title>Heron Creek Dental – Business Card</title>
<link rel="stylesheet" href="https://fonts.googleapis.com/css2?family=Open+Sans:wght@400;600;700&display=swap">
<style>
  :root {
    --brand-blue: #0255a3;
    --band-blue: #85acd3;
    --ink-blue: #0a4f98;
    --white: #ffffff;
    --line-white: rgba(255,255,255,0.75);
    --backdrop: #e9ecef;
  }
  * { box-sizing: border-box; margin: 0; padding: 0; }
  html, body { width: 800px; height: 1200px; overflow: hidden; }
  body {
    background: var(--backdrop);
    font-family: "Open Sans", Arial, sans-serif;
    position: relative;
  }
  .card {
    position: absolute;
    left: 50px;
    width: 700px;
    height: 400px;
    border-radius: 22px;
    background: var(--brand-blue);
    overflow: hidden;
    color: var(--white);
    box-shadow: 0 6px 18px rgba(0,0,0,0.18);
  }
  .card--front { top: 110px; }
  .card--back { top: 690px; }

  /* Front */
  .brand {
    position: absolute;
    top: 28px; left: 0; right: 0;
    display: flex; flex-direction: column; align-items: center; gap: 14px;
  }
  .brand__dot {
    width: 58px; height: 58px; border-radius: 50%;
    background: var(--white);
  }
  .brand__name {
    font-weight: 700; font-size: 22px; letter-spacing: 0.5px;
    text-transform: uppercase;
  }
  .identity-band {
    position: absolute;
    top: 150px; left: 0; right: 0; height: 112px;
    background: var(--band-blue);
    padding: 14px 0 0 44px;
    color: var(--ink-blue);
  }
  .identity-band__name {
    display: inline-block;
    font-weight: 700; font-size: 30px; text-transform: uppercase;
    border-bottom: 3px solid var(--ink-blue);
    padding-bottom: 2px; letter-spacing: 0.3px;
  }
  .identity-band__title {
    font-weight: 600; font-size: 27px; margin-top: 4px;
  }
  .contact { position: absolute; display: flex; align-items: center; gap: 12px; font-size: 19px; line-height: 1.25; }
  .contact svg { flex: none; }
  .contact--phone { top: 196px; right: 34px; }
  .contact--address { left: 40px; bottom: 38px; }
  .contact--web { left: 350px; bottom: 46px; }

  /* Back */
  .back-circle {
    position: absolute;
    right: -60px; top: -200px;
    width: 480px; height: 480px; border-radius: 50%;
    background: var(--white);
  }
  .appointment {
    position: absolute;
    top: 40px; left: 40px; width: 230px;
  }
  .appointment__label {
    font-weight: 700; font-size: 18px; letter-spacing: 1px;
    text-transform: uppercase; margin-bottom: 14px;
  }
  .appointment__field {
    display: flex; align-items: flex-end; gap: 10px;
    font-size: 16px; height: 38px;
  }
  .appointment__field span { width: 44px; }
  .appointment__field i {
    flex: 1; border-bottom: 1.5px solid var(--line-white); height: 1px;
    margin-bottom: 5px;
  }
  .back-name {
    position: absolute; left: 40px; bottom: 44px; z-index: 1;
    font-weight: 700; font-size: 42px; text-transform: uppercase; letter-spacing: 0.5px;
    white-space: nowrap;
  }
</style>
</head>
<body>

<section class="card card--front" aria-label="Business card front">
  <div class="brand">
    <span class="brand__dot"></span>
    <span class="brand__name">Heron Creek Dental</span>
  </div>

  <div class="identity-band">
    <span class="identity-band__name">Mira Castellan, DMD</span>
    <p class="identity-band__title">General &amp; Cosmetic Dentistry</p>
  </div>

  <div class="contact contact--phone">
    <svg width="30" height="30" viewBox="0 0 24 24" aria-hidden="true">
      <path fill="#ffffff" d="M6.6 10.8a15.1 15.1 0 0 0 6.6 6.6l2.2-2.2a1 1 0 0 1 1-.25 11.4 11.4 0 0 0 3.6.57 1 1 0 0 1 1 1V20a1 1 0 0 1-1 1A17 17 0 0 1 3 4a1 1 0 0 1 1-1h3.5a1 1 0 0 1 1 1c0 1.250.2 2.45.57 3.6a1 1 0 0 1-.25 1z"/>
    </svg>
    <div>5550142871<br>5550193604</div>
  </div>

  <div class="contact contact--address">
    <svg width="28" height="34" viewBox="0 0 24 30" aria-hidden="true">
      <path fill="none" stroke="#ffffff" stroke-width="2.4" d="M12 2a7 7 0 0 1 7 7c0 5-7 12-7 12S5 14 5 9a7 7 0 0 1 7-7z"/>
      <circle cx="12" cy="9" r="2.5" fill="#ffffff"/>
      <path fill="none" stroke="#ffffff" stroke-width="2.4" d="M6 22c-2 1-3 2-3 3 0 2 4 3 9 3s9-1 9-3c0-1-1-2-3-3"/>
    </svg>
    <div>2210 Alder Park Ave.<br>Fairview CA 90310</div>
  </div>

  <div class="contact contact--web">
    <svg width="30" height="30" viewBox="0 0 24 24" aria-hidden="true">
      <circle cx="12" cy="12" r="10" fill="none" stroke="#ffffff" stroke-width="1.8"/>
      <ellipse cx="12" cy="12" rx="4.5" ry="10" fill="none" stroke="#ffffff" stroke-width="1.5"/>
      <path d="M2 12h20M4 7h16M4 17h16" stroke="#ffffff" stroke-width="1.5"/>
    </svg>
    <span>heroncreekdentist.com</span>
  </div>
</section>

<section class="card card--back" aria-label="Business card back">
  <span class="back-circle"></span>
  <div class="appointment">
    <p class="appointment__label">Appointment</p>
    <div class="appointment__field"><span>Date</span><i></i></div>
    <div class="appointment__field"><span>Time</span><i></i></div>
  </div>
  <span class="back-name">Heron Creek Dental</span>
</section>

</body>
</html>
```